Brisken. business card

We need a business card design for a new mobile car-wash catered toward urban residents. The use of colour should be black, white and red and should be sleek and minimal. The final design should be modern and enticing to look at. A picture of the logo is attached. The font and design should resemble something similar to the logo.

```html
<!DOCTYPE html>
<html lang="en">
<head>
<meta charset="utf-8">
<title>Brisken. business card</title>
<link href="https://fonts.googleapis.com/css2?family=Open+Sans:wght@400;600;700&display=swap" rel="stylesheet">
<style>
  :root {
    --stage: #8f8f8f;
    --stage-dark: #3c3c3c;
    --card: #0d0d0d;
    --card-lift: #161616;
    --skyline-faint: #1e1e1e;
    --skyline: #3a3a3a;
    --skyline-deep: #2e2e2e;
    --band: #262626;
    --red: #e3141b;
    --white: #ffffff;
  }
  * { box-sizing: border-box; margin: 0; padding: 0; }
  html, body { width: 1200px; height: 900px; overflow: hidden; }
  body {
    font-family: "Open Sans", Arial, sans-serif;
    background: radial-gradient(ellipse at 30% 30%, #b5b5b5 0%, var(--stage) 45%, var(--stage-dark) 100%);
    display: flex;
    flex-direction: column;
    align-items: center;
    justify-content: center;
    gap: 40px;
  }
  .card {
    position: relative;
    width: 700px;
    height: 400px;
    background:
      radial-gradient(ellipse at 25% 20%, var(--card-lift) 0%, rgba(22,22,22,0) 60%),
      var(--card);
    overflow: hidden;
    box-shadow: 0 8px 24px rgba(0,0,0,.35);
  }

  /* Back side */
  .card-back .skyline-backdrop {
    position: absolute;
    left: 0; right: 0; bottom: 0;
    height: 340px;
    background:
      linear-gradient(90deg, rgba(13,13,13,.0) 0%, rgba(13,13,13,.35) 50%, rgba(13,13,13,0) 100%),
      linear-gradient(0deg, var(--skyline-faint) 0%, var(--skyline-faint) 55%, rgba(30,30,30,.6) 80%, rgba(30,30,30,0) 100%);
  }
  .card-back .brand-name {
    position: absolute;
    left: 0; right: 0; top: 50%;
    transform: translateY(-50%);
    text-align: center;
    color: var(--white);
    font-weight: 700;
    font-size: 68px;
    letter-spacing: 4px;
  }

  /* Front side */
  .card-front .brand-name {
    position: absolute;
    left: 40px; top: 34px;
    color: var(--red);
    font-weight: 700;
    font-size: 42px;
    letter-spacing: 3px;
    line-height: 1;
  }
  .card-front .divider {
    position: absolute;
    left: 36px; top: 100px;
    width: 340px; height: 2px;
    background: var(--white);
  }
  .card-front .person { position: absolute; left: 40px; top: 116px; }
  .person-name { color: var(--red); font-weight: 700; font-size: 22px; text-transform: uppercase; letter-spacing: .5px; }
  .person-role { color: var(--white); font-size: 14px; margin-top: 0; }
  .contacts {
    position: absolute; left: 40px; top: 200px;
    list-style: none;
  }
  .contacts li {
    display: flex; align-items: center; gap: 12px;
    color: var(--white); font-size: 15px; height: 24px;
  }
  .contacts svg { width: 16px; height: 16px; flex: none; }
  .skyline-block {
    position: absolute;
    left: 350px; right: 0; bottom: 0;
    height: 330px;
    background:
      linear-gradient(90deg, var(--skyline-deep) 0%, var(--skyline) 45%, var(--skyline) 80%, var(--skyline-deep) 100%);
    -webkit-mask-image: linear-gradient(0deg, #000 0%, #000 55%, rgba(0,0,0,.6) 80%, rgba(0,0,0,0) 100%);
            mask-image: linear-gradient(0deg, #000 0%, #000 55%, rgba(0,0,0,.6) 80%, rgba(0,0,0,0) 100%);
  }
  .address-band {
    position: absolute; left: 0; bottom: 0;
    width: 360px;
    height: 38px;
    background: var(--band);
    color: var(--white);
    font-weight: 700;
    font-size: 13px;
    text-transform: uppercase;
    padding-left: 40px;
    display: flex; align-items: center;
    white-space: nowrap;
  }
</style>
</head>
<body>

  <section class="card card-back" aria-label="Card back">
    <div class="skyline-backdrop" role="img" aria-label="Faint city skyline silhouette across the card"></div>
    <div class="brand-name">Brisken.</div>
  </section>

  <section class="card card-front" aria-label="Card front">
    <div class="skyline-block" role="img" aria-label="Grey city skyline silhouette rising from the bottom right"></div>
    <div class="brand-name">Brisken.</div>
    <div class="divider"></div>
    <div class="person">
      <div class="person-name">Marcus Hale</div>
      <div class="person-role">Director</div>
    </div>
    <ul class="contacts">
      <li>
        <svg viewBox="0 0 16 16"><rect width="16" height="16" rx="2" fill="var(--red)"/><rect x="5" y="3" width="6" height="10" rx="1" fill="none" stroke="#fff" stroke-width="1.3"/></svg>
        0912 348 765
      </li>
      <li>
        <svg viewBox="0 0 16 16"><rect width="16" height="16" rx="2" fill="var(--red)"/><path d="M5 3.5c-1 1-1 3 1 5.5s4.5 3 5.5 2l-1.5-1.8-1.3.8c-1-.5-2-1.6-2.5-2.6l.8-1.3z" fill="#fff"/></svg>
        0156 273 840
      </li>
      <li>
        <svg viewBox="0 0 16 16"><rect width="16" height="16" rx="2" fill="var(--red)"/><rect x="3" y="4.5" width="10" height="7" fill="none" stroke="#fff" stroke-width="1.2"/><path d="M3 4.5l5 4 5-4" fill="none" stroke="#fff" stroke-width="1.2"/></svg>
        marcushale@brisken.com
      </li>
      <li>
        <svg viewBox="0 0 16 16"><rect width="16" height="16" rx="2" fill="var(--red)"/><circle cx="8" cy="8" r="4.5" fill="none" stroke="#fff" stroke-width="1.2"/><path d="M3.5 8h9M8 3.5c-2 2.5-2 6.5 0 9M8 3.5c2 2.5 2 6.5 0 9" fill="none" stroke="#fff" stroke-width="1"/></svg>
        www.brisken.com
      </li>
    </ul>
    <div class="address-band">482 Harbor Lane, Eastgate, Metro City</div>
  </section>

</body>
</html>
```